Emergency Medical Training and Events Company Business Needs Business Card Design

We are in need of a business card for our dynamic company expanding its customer base and need to be easily contacted and identified for when we visit with government officials, potential EMS / Fire agencies and county coordinators to arrange for training programs for first responders to better prepare them for critical thinking at critical incidents.

Target Market(s)

EMS/Fire and Event Promoters

Industry/Entity Type

Medical

Contact Information for Business Card

Two cards, comparable designs:

Martin K. Halvey, Principal, m.halvey@rvqtlo.com
Owen Tash, Event and Training Specialist, o.tash@rvqtlo.com

Font styles to use
Other font styles liked:
• Cambria

Colors

Designer to choose colors to be used in the design.

Requirements
Must have
• Company Logo, Spots for Name, Title, Phone Number, Email, Website
• A bullet list stating that we offer, QRB CPR and First Aid Instructors, Hold the Line Instructors, Event EMS, CME's, MCI Training and Planning. We prefer to have a black background for the card but if you can make a blue or white card stand out we would review that as well.
Should not have
• Tacky logos or special sayings ... simple, elegant, professional is the look we seek

```html
<!DOCTYPE html>
<html lang="en">
<head>
<meta charset="utf-8">
<title>R.V.Q.T. Lifeline Ops – Business Cards</title>
<link rel="stylesheet" href="https://fonts.googleapis.com/css2?family=Montserrat:wght@400;500;600;700&display=swap">
<style>
  :root {
    --stage: #1c1c1c;
    --stage-light: #333333;
    --navy: #0b1a56;
    --navy-deep: #08133f;
    --navy-soft: #13246a;
    --red: #d3202a;
    --white: #ffffff;
  }
  * { margin: 0; padding: 0; box-sizing: border-box; }
  html, body { width: 1200px; height: 900px; overflow: hidden; }
  body {
    background: radial-gradient(ellipse at 50% 30%, var(--stage-light), var(--stage) 75%);
    font-family: "Montserrat", sans-serif;
    color: var(--white);
    position: relative;
  }
  .card {
    position: absolute;
    left: 250px;
    width: 700px;
    height: 400px;
    background: linear-gradient(135deg, var(--navy) 0%, var(--navy-deep) 100%);
    overflow: hidden;
    box-shadow: 0 18px 40px rgba(0,0,0,.6);
  }
  .card--back { top: 30px; }
  .card--front { top: 470px; }

  .card__watermark {
    position: absolute;
    left: -70px;
    top: 40px;
    width: 330px;
    height: 330px;
    border-radius: 50%;
    background: var(--navy-soft);
    opacity: .55;
  }

  .brand {
    position: absolute;
    left: 330px;
    top: 58px;
    display: flex;
    align-items: center;
    gap: 14px;
  }
  .brand__dot {
    width: 64px; height: 64px;
    border-radius: 50%;
    background: var(--white);
    flex: none;
  }
  .brand__name {
    font-weight: 700;
    font-size: 26px;
    line-height: 1.15;
    letter-spacing: .5px;
    color: var(--white);
    text-transform: uppercase;
  }

  .services {
    position: absolute;
    left: 330px;
    top: 205px;
    list-style: none;
    font-size: 18px;
    font-weight: 500;
    line-height: 26px;
  }
  .services li { position: relative; padding-left: 20px; }
  .services li::before {
    content: "";
    position: absolute;
    left: 0; top: 9px;
    width: 9px; height: 9px;
    border-radius: 50%;
    background: var(--red);
  }

  .person {
    position: absolute;
    left: 330px;
    top: 160px;
  }
  .person__name {
    font-size: 34px;
    font-weight: 600;
    letter-spacing: 1px;
    text-transform: uppercase;
  }
  .person__title {
    font-size: 20px;
    color: var(--red);
    margin-top: -2px;
  }
  .person__rule {
    width: 345px;
    height: 2px;
    background: var(--red);
    margin-top: 10px;
  }

  .contact {
    position: absolute;
    left: 330px;
    top: 268px;
    list-style: none;
    font-size: 21px;
    line-height: 30px;
  }
  .contact li { display: flex; align-items: center; gap: 12px; }
  .contact svg { width: 20px; height: 20px; flex: none; }
  .contact__site strong { color: var(--red); font-weight: 700; }

  .card__band {
    position: absolute;
    left: 0; bottom: 0;
    width: 700px; height: 40px;
  }
</style>
</head>
<body>

  <section class="card card--back" aria-label="Card back with services">
    <div class="card__watermark"></div>
    <div class="brand">
      <span class="brand__dot"></span>
      <span class="brand__name">R.V.Q.T.<br>Lifeline Ops</span>
    </div>
    <ul class="services">
      <li>QRB CPR and First Aid Instructors</li>
      <li>Hold the Line Instructors</li>
      <li>Event EMS</li>
      <li>CME’s</li>
      <li>MCI Training and Planning</li>
    </ul>
  </section>

  <section class="card card--front" aria-label="Card front with contact details">
    <div class="card__watermark"></div>
    <div class="brand">
      <span class="brand__dot"></span>
      <span class="brand__name">R.V.Q.T.<br>Lifeline Ops</span>
    </div>
    <div class="person">
      <p class="person__name">Owen Tash</p>
      <p class="person__title">Event and Training Specialist</p>
      <div class="person__rule"></div>
    </div>
    <ul class="contact">
      <li>
        <svg viewBox="0 0 24 24" fill="none" stroke="#d3202a" stroke-width="2" stroke-linecap="round" stroke-linejoin="round"><circle cx="12" cy="12" r="10"/><path d="M8.5 7.5c0 4.5 3.5 8 8 8l1-2-2.5-1.2-1 1c-1.6-.7-2.6-1.7-3.3-3.3l1-1L10.5 6.5z"/></svg>
        <span>555.014.2290</span>
      </li>
      <li>
        <svg viewBox="0 0 24 24" fill="none" stroke="#d3202a" stroke-width="2" stroke-linejoin="round"><rect x="2" y="5" width="20" height="14"/><path d="M2 5l10 8 10-8"/></svg>
        <span>o.tash@rvqtlo.com</span>
      </li>
      <li>
        <svg viewBox="0 0 24 24" fill="none" stroke="#d3202a" stroke-width="2"><circle cx="12" cy="12" r="10"/><ellipse cx="12" cy="12" rx="4" ry="10"/><path d="M2 12h20M4 7h16M4 17h16"/></svg>
        <span class="contact__site">www.<strong>rvqtlo</strong>.com</span>
      </li>
    </ul>
    <svg class="card__band" viewBox="0 0 700 40" preserveAspectRatio="none" aria-hidden="true">
      <polygon points="440,10 700,10 700,40 470,40" fill="#ffffff"/>
    </svg>
  </section>

</body>
</html>
```